Powerpoint design for european B2B business

We need a Powerpoint design for a newly established IT company with a B2B focus. We want to develop management information systems that help managers communicate goals into their organization and analyze their organizational activities and performance.

We defined the attached color scale, please relate your design to these colors.

The design should be simple and straight, serious and professional and leave enough space for the content ... :-)

Target Market(s)

B2B, companies larger than 200 employees

Industry/Entity Type

Business

Font styles to use
Sans Serif

Requirements
Should not have
• too playful design, clipart style

```html
<!DOCTYPE html>
<html lang="en">
<head>
<meta charset="utf-8">
<title>Slide Design Idea - 01a</title>
<link rel="stylesheet" href="https://fonts.googleapis.com/css2?family=Arimo:wght@400;700&family=Open+Sans:wght@400;600;700&display=swap">
<style>
:root{
  --bg:#3b1212;
  --head:#6e5151;
  --sub:#8d6c6c;
  --panel:#ffffff;
  --teal:#1b9e85;
  --orange:#f39c1b;
  --navy:#3c5a82;
  --slate:#3f4e66;
  --red:#d8352a;
  --green:#8cc63f;
  --blue:#2a8cc9;
  --yellow:#f5c518;
  --ph:#c9c9c9;
  --line:#d8d8d8;
  --ink:#555;
  --brandink:#2b4a70;
}
*{box-sizing:border-box;margin:0;padding:0}
html,body{width:1200px;height:930px;overflow:hidden}
body{background:var(--bg);font-family:"Open Sans",Arial,sans-serif;position:relative}
.sheet-title{position:absolute;top:28px;left:0;width:1200px;text-align:center;font-family:"Arimo",Arial,sans-serif;font-weight:700;font-size:33px;color:var(--head)}
.sheet-note{position:absolute;top:82px;left:0;width:1200px;text-align:center;font-family:"Arimo",Arial,sans-serif;font-size:19.5px;line-height:24px;color:var(--sub)}
.board{position:absolute;top:166px;left:8px;width:1182px;height:738px;background:var(--panel);padding:8px 10px 0;display:grid;grid-template-columns:repeat(6,175px);column-gap:23.4px;grid-auto-rows:121.6px}
.cell{display:flex;flex-direction:column;align-items:center}
.file{margin-top:6px;font-size:8.5px;color:#222;font-family:"Arimo",Arial,sans-serif}
.slide{position:relative;width:175px;height:98px;background:#fff;box-shadow:0 1px 3px rgba(0,0,0,.35);overflow:hidden;font-size:3px;color:var(--ink)}
.a{position:absolute}
.st{position:absolute;top:8px;left:0;width:100%;text-align:center;font-size:6.5px;color:#666}
.brand{position:absolute;top:5px;right:6px;font-size:6.5px;font-weight:700;color:var(--brandink)}
.mark{position:absolute;top:3px;left:3px;width:5px;height:5px;background:var(--teal)}
.ph{position:absolute;background:var(--ph)}
.copy{position:absolute;background:repeating-linear-gradient(var(--line) 0 1px,transparent 1px 3px)}
.pager{position:absolute;bottom:4px;left:50%;transform:translateX(-50%);width:20px;height:3px;background:radial-gradient(circle,var(--red) 1px,transparent 1.3px) 0 0/4px 3px repeat-x}
.ic{position:absolute;width:8px;height:8px;border-radius:50%}
.lb{position:absolute;font-size:3px;color:#333;white-space:nowrap}
.w{color:#fff}
.teal{background:var(--teal)}.orange{background:var(--orange)}.navy{background:var(--navy)}.red{background:var(--red)}.green{background:var(--green)}.blue{background:var(--blue)}.slate{background:var(--slate)}.yellow{background:var(--yellow)}
.photo{position:absolute;background:linear-gradient(160deg,#6e8db2,#2f4f78 60%,#1d3556)}
.big-title{position:absolute;width:100%;text-align:center;font-weight:700;color:#fff}
.defs{position:absolute;width:0;height:0}
</style>
</head>
<body>
<svg class="defs" aria-hidden="true">
  <defs>
    <pattern id="dotGray" width="6" height="6" patternUnits="userSpaceOnUse"><circle cx="3" cy="3" r="2.3" fill="#cfd6dc"/></pattern>
    <pattern id="dotRed" width="6" height="6" patternUnits="userSpaceOnUse"><circle cx="3" cy="3" r="2.3" fill="#d8352a"/></pattern>
    <pattern id="dotYellow" width="6" height="6" patternUnits="userSpaceOnUse"><circle cx="3" cy="3" r="2.3" fill="#f5c518"/></pattern>
    <pattern id="dotTeal" width="6" height="6" patternUnits="userSpaceOnUse"><circle cx="3" cy="3" r="2.3" fill="#1b9e85"/></pattern>
    <pattern id="tileBlue" width="7" height="5" patternUnits="userSpaceOnUse"><rect x="0.5" y="0.5" width="5.5" height="3.5" fill="none" stroke="#2a8cc9" stroke-width=".6"/></pattern>
    <pattern id="tileGreen" width="7" height="5" patternUnits="userSpaceOnUse"><rect x="0.5" y="0.5" width="5.5" height="3" fill="#1b9e85"/></pattern>
    <pattern id="tileOrange" width="7" height="5" patternUnits="userSpaceOnUse"><rect x="0.5" y="0.5" width="4" height="3.5" fill="#f39c1b"/></pattern>
    <symbol id="house" viewBox="0 0 10 10"><polygon points="0,5 5,0 10,5 8.5,5 8.5,10 1.5,10 1.5,5"/></symbol>
  </defs>
</svg>

<h1 class="sheet-title">Slide Design Idea - 01a</h1>
<p class="sheet-note">Fonts, Colors, Images, content placements are changeable<br>( 16:9 format) . Please note that I have used an image placeholder on all the slides instead of using sample images</p>

<main class="board">

  <!-- 1 -->
  <div class="cell"><div class="slide">
    <div class="a slate" style="left:0;top:0;width:175px;height:42px"></div>
    <div class="big-title" style="top:15px;font-size:6.5px">PRESENTATION TITLE</div>
    <div class="big-title" style="top:26px;font-size:3.5px;color:var(--orange)">PRESENTATION SUB TITLE</div>
    <div class="a" style="top:52px;left:0;width:175px;text-align:center;font-size:18px;font-weight:700;color:var(--brandink)">Norvalo</div>
    <div class="a" style="top:74px;left:0;width:175px;text-align:center;font-size:3px;color:#888">MANAGEMENT INFORMATION SYSTEMS</div>
  </div><span class="file">Slide1.JPG</span></div>

  <!-- 2 -->
  <div class="cell"><div class="slide">
    <div class="a" style="top:3px;left:0;width:175px;text-align:center;font-size:15px;font-weight:700;color:var(--brandink)">Norvalo</div>
    <div class="photo" style="left:0;top:28px;width:175px;height:44px;background:linear-gradient(180deg,#8ea3bd,#4d6a8e)" role="img" aria-label="Photo of glass office towers"></div>
    <div class="a" style="top:80px;left:0;width:175px;text-align:center;font-size:6.5px;font-weight:700;color:#333">ENTER YOUR PRESENTATION TITLE</div>
  </div><span class="file">Slide2.JPG</span></div>

  <!-- 3 -->
  <div class="cell"><div class="slide" style="background:#1f3d66">
    <div class="photo" style="left:0;top:0;width:175px;height:98px" role="img" aria-label="Photo of office towers against the sky"></div>
    <div class="big-title" style="top:8px;font-size:6.5px">ENTER YOUR PRESENTATION TITLE</div>
    <div class="a" style="left:62px;top:35px;width:50px;height:50px;border-radius:50%;background:#fff"></div>
    <div class="a" style="left:62px;top:53px;width:50px;text-align:center;font-size:10px;font-weight:700;color:var(--brandink)">Norvalo</div>
  </div><span class="file">Slide3.JPG</span></div>

  <!-- 4 -->
  <div class="cell"><div class="slide">
    <div class="photo" style="left:0;top:0;width:175px;height:98px;background:linear-gradient(160deg,#2c4f86,#16305a 70%,#0f2446)" role="img" aria-label="Photo of office towers at dusk"></div>
    <div class="big-title" style="top:8px;font-size:6.5px">ENTER YOUR PRESENTATION TITLE</div>
    <div class="a" style="left:62px;top:35px;width:50px;height:50px;border-radius:50%;background:#fff"></div>
    <div class="a" style="left:62px;top:53px;width:50px;text-align:center;font-size:10px;font-weight:700;color:var(--brandink)">Norvalo</div>
  </div><span class="file">Slide4.JPG</span></div>

  <!-- 5 -->
  <div class="cell"><div class="slide">
    <div class="photo" style="left:0;top:0;width:175px;height:98px;background:linear-gradient(150deg,#58738f,#2a4565)" role="img" aria-label="Photo of high-rise office buildings"></div>
    <svg class="a" style="left:0;top:14px" width="175" height="20" aria-hidden="true"><polygon points="12,2 168,2 160,18 12,18" fill="#2b4a7d"/><polygon points="168,2 172,2 164,18 160,18" fill="#f39c1b"/></svg>
    <div class="a w" style="left:45px;top:20px;font-size:6.5px;font-weight:700">PRESENTATION TITLE</div>
    <div class="a" style="left:0;top:66px;width:76px;height:18px;background:#fff;border-radius:0 9px 9px 0"></div>
    <div class="a" style="left:16px;top:68px;font-size:10px;font-weight:700;color:var(--brandink)">Norvalo</div>
  </div><span class="file">Slide5.JPG</span></div>

  <!-- 6 -->
  <div class="cell"><div class="slide">
    <i class="mark"></i><div class="st">About Us</div><div class="brand">Norvalo</div>
    <div class="ph" style="left:8px;top:20px;width:58px;height:52px"></div>
    <i class="ic red" style="left:90px;top:20px"></i><span class="lb" style="left:88px;top:30px">Digital</span><div class="copy" style="left:80px;top:34px;width:28px;height:6px"></div>
    <i class="ic orange" style="left:142px;top:20px"></i><span class="lb" style="left:141px;top:30px">Mobile</span><div class="copy" style="left:132px;top:34px;width:28px;height:6px"></div>
    <i class="ic green" style="left:90px;top:46px"></i><span class="lb" style="left:88px;top:56px">System</span><div class="copy" style="left:80px;top:60px;width:28px;height:6px"></div>
    <i class="ic blue" style="left:142px;top:46px"></i><span class="lb" style="left:138px;top:56px">Innovation</span><div class="copy" style="left:132px;top:60px;width:28px;height:6px"></div>
    <div class="copy" style="left:10px;top:80px;width:155px;height:4px"></div><i class="pager"></i>
  </div><span class="file">Slide6.JPG</span></div>

  <!-- 7 -->
  <div class="cell"><div class="slide">
    <i class="mark"></i><div class="st">Our Team</div><div class="brand">Norvalo</div>
    <div class="ph" style="left:12px;top:18px;width:46px;height:28px"></div>
    <div class="ph" style="left:65px;top:18px;width:46px;height:28px"></div>
    <div class="ph" style="left:118px;top:18px;width:46px;height:28px"></div>
    <div class="a teal" style="left:0;top:46px;width:175px;height:16px"></div>
    <span class="lb w" style="left:12px;top:49px;width:46px;text-align:center">Member Name</span><span class="lb w" style="left:65px;top:49px;width:46px;text-align:center">Member Name</span><span class="lb w" style="left:118px;top:49px;width:46px;text-align:center">Member Name</span>
    <span class="lb w" style="left:12px;top:54px;width:46px;text-align:center">Project Manager</span><span class="lb w" style="left:65px;top:54px;width:46px;text-align:center">Designer</span><span class="lb w" style="left:118px;top:54px;width:46px;text-align:center">Developer</span>
    <div class="copy" style="left:12px;top:66px;width:46px;height:9px"></div><div class="copy" style="left:65px;top:66px;width:46px;height:9px"></div><div class="copy" style="left:118px;top:66px;width:46px;height:9px"></div>
    <i class="pager"></i>
  </div><span class="file">Slide7.JPG</span></div>

  <!-- 8 -->
  <div class="cell"><div class="slide">
    <i class="mark"></i><div class="st">Our Philosophy</div><div class="brand">Norvalo</div>
    <i class="ic red" style="left:30px;top:22px"></i><span class="lb" style="left:28px;top:32px">Good Value</span>
    <i class="ic orange" style="left:83px;top:22px"></i><span class="lb" style="left:80px;top:32px">More Awards</span>
    <i class="ic green" style="left:136px;top:22px"></i><span class="lb" style="left:132px;top:32px">Top of Market</span>
    <i class="ic teal" style="left:30px;top:48px"></i><span class="lb" style="left:25px;top:58px">Hidden Strategy</span>
    <i class="ic slate" style="left:83px;top:48px"></i><span class="lb" style="left:77px;top:58px">Well Document</span>
    <i class="ic navy" style="left:136px;top:48px"></i><span class="lb" style="left:131px;top:58px">More Growth</span>
    <div class="copy" style="left:12px;top:70px;width:150px;height:6px"></div><i class="pager"></i>
  </div><span class="file">Slide8.JPG</span></div>

  <!-- 9 -->
  <div class="cell"><div class="slide">
    <i class="mark"></i><div class="st">Bullet Style - 1</div><div class="brand">Norvalo</div>
    <div class="ph" style="left:14px;top:22px;width:48px;height:58px"></div>
    <span class="lb" style="left:72px;top:22px;font-weight:700">Sub Heading</span>
    <div class="copy" style="left:72px;top:28px;width:88px;height:10px"></div>
    <div class="copy" style="left:76px;top:42px;width:80px;height:30px"></div>
  </div><span class="file">Slide9.JPG</span></div>

  <!-- 10 -->
  <div class="cell"><div class="slide">
    <i class="mark"></i><div class="st">Bullet Style - 2</div><div class="brand">Norvalo</div>
    <span class="lb" style="left:12px;top:19px;font-weight:700">List Style Within List</span>
    <div class="copy" style="left:12px;top:25px;width:150px;height:8px"></div>
    <div class="copy" style="left:18px;top:37px;width:110px;height:22px"></div>
    <div class="copy" style="left:24px;top:62px;width:96px;height:14px"></div>
  </div><span class="file">Slide10.JPG</span></div>

  <!-- 11 -->
  <div class="cell"><div class="slide">
    <i class="mark"></i><div class="st">Individual Skill</div><div class="brand">Norvalo</div>
    <div class="ph" style="left:14px;top:22px;width:48px;height:56px"></div>
    <span class="lb" style="left:90px;top:22px;font-weight:700">Member Name</span>
    <div class="copy" style="left:90px;top:30px;width:14px;height:36px"></div>
    <svg class="a" style="left:108px;top:28px" width="60" height="42" aria-hidden="true">
      <rect width="60" height="42" fill="url(#dotGray)"/>
      <rect width="36" height="6" fill="url(#dotRed)"/>
      <rect y="6" width="48" height="6" fill="url(#dotYellow)"/>
      <rect y="12" width="30" height="6" fill="url(#dotYellow)"/>
      <rect y="18" width="42" height="6" fill="url(#dotTeal)"/>
      <rect y="24" width="54" height="6" fill="url(#dotTeal)"/>
      <rect y="30" width="36" height="6" fill="url(#dotTeal)"/>
      <rect y="36" width="60" height="6" fill="url(#dotTeal)"/>
    </svg>
  </div><span class="file">Slide11.JPG</span></div>

  <!-- 12 -->
  <div class="cell"><div class="slide">
    <i class="mark"></i><div class="st">Personality</div><div class="brand">Norvalo</div>
    <div class="ph" style="left:70px;top:20px;width:36px;height:58px"></div>
    <i class="ic orange" style="left:58px;top:24px;width:6px;height:6px"></i><div class="copy" style="left:22px;top:24px;width:32px;height:6px"></div>
    <i class="ic red" style="left:58px;top:38px;width:6px;height:6px"></i><div class="copy" style="left:22px;top:38px;width:32px;height:6px"></div>
    <i class="ic green" style="left:58px;top:52px;width:6px;height:6px"></i><div class="copy" style="left:22px;top:52px;width:32px;height:6px"></div>
    <i class="ic blue" style="left:58px;top:66px;width:6px;height:6px"></i><div class="copy" style="left:22px;top:66px;width:32px;height:6px"></div>
    <i class="ic orange" style="left:112px;top:24px;width:6px;height:6px"></i><div class="copy" style="left:122px;top:24px;width:32px;height:6px"></div>
    <i class="ic red" style="left:112px;top:38px;width:6px;height:6px"></i><div class="copy" style="left:122px;top:38px;width:32px;height:6px"></div>
    <i class="ic green" style="left:112px;top:52px;width:6px;height:6px"></i><div class="copy" style="left:122px;top:52px;width:32px;height:6px"></div>
    <i class="ic blue" style="left:112px;top:66px;width:6px;height:6px"></i><div class="copy" style="left:122px;top:66px;width:32px;height:6px"></div>
  </div><span class="file">Slide12.JPG</span></div>

  <!-- 13 -->
  <div class="cell"><div class="slide">
    <i class="mark"></i><div class="st">Development</div><div class="brand">Norvalo</div>
    <div class="a teal" style="left:0;top:68px;width:175px;height:30px"></div>
    <div class="ph" style="left:72px;top:20px;width:32px;height:56px"></div>
    <i class="ic orange" style="left:58px;top:30px"></i><div class="copy" style="left:18px;top:30px;width:36px;height:8px"></div>
    <i class="ic blue" style="left:58px;top:48px"></i><div class="copy" style="left:18px;top:48px;width:36px;height:8px"></div>
    <i class="ic red" style="left:110px;top:30px"></i><div class="copy" style="left:122px;top:30px;width:36px;height:8px"></div>
    <i class="ic green" style="left:110px;top:48px"></i><div class="copy" style="left:122px;top:48px;width:36px;height:8px"></div>
    <div class="copy" style="left:14px;top:82px;width:148px;height:7px;background:repeating-linear-gradient(rgba(255,255,255,.6) 0 1px,transparent 1px 3px)"></div>
  </div><span class="file">Slide13.JPG</span></div>

  <!-- 14 -->
  <div class="cell"><div class="slide">
    <i class="mark"></i><div class="st">Portfolio</div><div class="brand">Norvalo</div>
    <div class="ph" style="left:10px;top:22px;width:34px;height:32px;border-bottom:2px solid var(--blue)"></div>
    <div class="ph" style="left:51px;top:22px;width:34px;height:32px;border-bottom:2px solid var(--green)"></div>
    <div class="ph" style="left:92px;top:22px;width:34px;height:32px;border-bottom:2px solid var(--orange)"></div>
    <div class="ph" style="left:133px;top:22px;width:34px;height:32px;border-bottom:2px solid var(--red)"></div>
    <div class="copy" style="left:10px;top:58px;width:34px;height:9px"></div><div class="copy" style="left:51px;top:58px;width:34px;height:9px"></div><div class="copy" style="left:92px;top:58px;width:34px;height:9px"></div><div class="copy" style="left:133px;top:58px;width:34px;height:9px"></div>
    <i class="pager" style="bottom:22px"></i><div class="copy" style="left:14px;top:82px;width:148px;height:6px"></div>
  </div><span class="file">Slide14.JPG</span></div>

  <!-- 15 -->
  <div class="cell"><div class="slide">
    <i class="mark"></i><div class="st">Our Capabilities</div><div class="brand">Norvalo</div>
    <svg class="a" style="left:0;top:20px" width="175" height="30" aria-hidden="true" fill="none" stroke="#333" stroke-width="1.2">
      <rect x="20" y="6" width="28" height="18"/><line x1="16" y1="26" x2="52" y2="26"/>
      <rect x="73" y="6" width="28" height="18"/><line x1="69" y1="26" x2="105" y2="26"/>
      <rect x="127" y="6" width="28" height="18"/><line x1="123" y1="26" x2="159" y2="26"/>
    </svg>
    <div class="a orange" style="left:0;top:52px;width:175px;height:8px"></div>
    <span class="lb w" style="left:24px;top:54px">TRAINING</span><span class="lb w" style="left:76px;top:54px">UPGRADING</span><span class="lb w" style="left:130px;top:54px">COMPOSING</span>
    <div class="copy" style="left:14px;top:64px;width:40px;height:12px"></div><div class="copy" style="left:67px;top:64px;width:40px;height:12px"></div><div class="copy" style="left:121px;top:64px;width:40px;height:12px"></div>
    <i class="pager"></i>
  </div><span class="file">Slide15.JPG</span></div>

  <!-- 16 -->
  <div class="cell"><div class="slide">
    <i class="mark"></i><div class="st">Company Engagement</div><div class="brand">Norvalo</div>
    <div class="a teal" style="left:0;top:42px;width:175px;height:56px"></div>
    <div class="ph" style="left:14px;top:26px;width:32px;height:30px"></div>
    <div class="ph" style="left:53px;top:26px;width:32px;height:30px"></div>
    <div class="ph" style="left:92px;top:26px;width:32px;height:30px"></div>
    <div class="ph" style="left:131px;top:26px;width:32px;height:30px"></div>
    <span class="lb w" style="left:16px;top:62px">SPECIAL I</span><span class="lb w" style="left:55px;top:62px">SPECIAL II</span><span class="lb w" style="left:94px;top:62px">SPECIAL III</span><span class="lb w" style="left:133px;top:62px">SPECIAL IV</span>
    <div class="copy" style="left:16px;top:68px;width:30px;height:12px;background:repeating-linear-gradient(rgba(255,255,255,.6) 0 1px,transparent 1px 3px)"></div>
    <div class="copy" style="left:55px;top:68px;width:30px;height:12px;background:repeating-linear-gradient(rgba(255,255,255,.6) 0 1px,transparent 1px 3px)"></div>
    <div class="copy" style="left:94px;top:68px;width:30px;height:12px;background:repeating-linear-gradient(rgba(255,255,255,.6) 0 1px,transparent 1px 3px)"></div>
    <div class="copy" style="left:133px;top:68px;width:30px;height:12px;background:repeating-linear-gradient(rgba(255,255,255,.6) 0 1px,transparent 1px 3px)"></div>
  </div><span class="file">Slide16.JPG</span></div>

  <!-- 17 -->
  <div class="cell"><div class="slide">
    <i class="mark"></i><div class="st">Portfolio</div><div class="brand">Norvalo</div>
    <div class="ph" style="left:18px;top:18px;width:30px;height:18px"></div><div class="ph" style="left:55px;top:18px;width:30px;height:18px"></div><div class="ph" style="left:92px;top:18px;width:30px;height:18px"></div><div class="ph" style="left:129px;top:18px;width:30px;height:18px"></div>
    <div class="copy" style="left:18px;top:39px;width:30px;height:8px"></div><div class="copy" style="left:55px;top:39px;width:30px;height:8px"></div><div class="copy" style="left:92px;top:39px;width:30px;height:8px"></div><div class="copy" style="left:129px;top:39px;width:30px;height:8px"></div>
    <div class="ph" style="left:18px;top:50px;width:30px;height:18px"></div><div class="ph" style="left:55px;top:50px;width:30px;height:18px"></div><div class="ph" style="left:92px;top:50px;width:30px;height:18px"></div><div class="ph" style="left:129px;top:50px;width:30px;height:18px"></div>
    <div class="copy" style="left:18px;top:71px;width:30px;height:8px"></div><div class="copy" style="left:55px;top:71px;width:30px;height:8px"></div><div class="copy" style="left:92px;top:71px;width:30px;height:8px"></div><div class="copy" style="left:129px;top:71px;width:30px;height:8px"></div>
  </div><span class="file">Slide17.JPG</span></div>

  <!-- 18 -->
  <div class="cell"><div class="slide">
    <i class="mark"></i><div class="st">Portfolio</div><div class="brand">Norvalo</div>
    <div class="ph" style="left:0;top:20px;width:44px;height:30px"></div>
    <div class="a teal" style="left:44px;top:20px;width:44px;height:30px"></div>
    <div class="ph" style="left:88px;top:20px;width:43px;height:30px"></div>
    <div class="a orange" style="left:131px;top:20px;width:44px;height:30px"></div>
    <div class="a blue" style="left:0;top:50px;width:44px;height:28px"></div>
    <div class="a green" style="left:88px;top:50px;width:43px;height:28px"></div>
    <div class="ph" style="left:44px;top:50px;width:44px;height:28px"></div>
    <div class="a red" style="left:131px;top:50px;width:44px;height:28px"></div>
    <span class="lb w" style="left:52px;top:24px">Portfolio II</span><span class="lb w" style="left:138px;top:24px">Portfolio IV</span><span class="lb w" style="left:6px;top:54px">Portfolio I</span><span class="lb w" style="left:95px;top:54px">Portfolio III</span><span class="lb w" style="left:138px;top:54px">Portfolio V</span>
    <i class="pager"></i>
  </div><span class="file">Slide18.JPG</span></div>

  <!-- 19 -->
  <div class="cell"><div class="slide">
    <i class="mark"></i><div class="st">Our Philosophy</div><div class="brand">Norvalo</div>
    <div class="a orange" style="left:60px;top:18px;width:96px;height:18px"></div>
    <div class="a green" style="left:60px;top:38px;width:96px;height:18px"></div>
    <div class="a teal" style="left:60px;top:58px;width:96px;height:18px"></div>
    <span class="lb w" style="left:80px;top:21px">Clean Look</span><span class="lb w" style="left:80px;top:41px">Shared Communication</span><span class="lb w" style="left:80px;top:61px">Researching</span>
    <i class="ic blue" style="left:28px;top:34px"></i><div class="copy" style="left:18px;top:46px;width:30px;height:6px"></div>
    <i class="ic blue" style="left:160px;top:34px"></i>
  </div><span class="file">Slide19.JPG</span></div>

  <!-- 20 -->
  <div class="cell"><div class="slide">
    <i class="mark"></i><div class="st">Board Philosophy</div><div class="brand">Norvalo</div>
    <div class="a red" style="left:0;top:20px;width:35px;height:34px"></div>
    <div class="a orange" style="left:35px;top:20px;width:35px;height:34px"></div>
    <div class="a green" style="left:70px;top:20px;width:35px;height:34px"></div>
    <div class="a teal" style="left:105px;top:20px;width:35px;height:34px"></div>
    <div class="a blue" style="left:140px;top:20px;width:35px;height:34px"></div>
    <svg class="a" style="left:0;top:30px" width="175" height="14" aria-hidden="true" fill="none" stroke="#fff" stroke-width="1.2">
      <circle cx="17.5" cy="7" r="5"/><rect x="45" y="2" width="15" height="9"/><polygon points="87.5,1 93,12 82,12"/><circle cx="122.5" cy="7" r="4"/><rect x="154" y="2" width="7" height="10"/>
    </svg>
    <span class="lb" style="left:8px;top:58px">Situation</span><span class="lb" style="left:42px;top:58px">Cloud Icon</span><span class="lb" style="left:79px;top:58px">Position</span><span class="lb" style="left:113px;top:58px">Document</span><span class="lb" style="left:148px;top:58px">Look List</span>
    <div class="copy" style="left:4px;top:63px;width:166px;height:10px"></div><i class="pager"></i>
  </div><span class="file">Slide20.JPG</span></div>

  <!-- 21 -->
  <div class="cell"><div class="slide">
    <i class="mark"></i><div class="st">Special Product</div><div class="brand">Norvalo</div>
    <div class="a teal" style="left:12px;top:22px;width:80px;height:34px"></div>
    <div class="ph" style="left:92px;top:22px;width:72px;height:34px"></div>
    <span class="lb w" style="left:40px;top:26px">Rising Patient</span><div class="copy" style="left:18px;top:31px;width:68px;height:18px;background:repeating-linear-gradient(rgba(255,255,255,.6) 0 1px,transparent 1px 3px)"></div>
    <svg class="a" style="left:0;top:60px" width="175" height="12" aria-hidden="true">
      <rect x="30" y="4" width="1.5" height="7" fill="#1b9e85"/><rect x="33" y="2" width="1.5" height="9" fill="#1b9e85"/><rect x="36" y="5" width="1.5" height="6" fill="#1b9e85"/>
      <rect x="76" y="4" width="7" height="7" fill="#8cc63f"/><ellipse cx="120" cy="7" rx="5" ry="3" fill="#f39c1b"/><circle cx="158" cy="5" r="3.5" fill="#d8352a"/>
    </svg>
    <span class="lb" style="left:24px;top:74px">Ultimate Time</span><span class="lb" style="left:74px;top:74px">Limited</span><span class="lb" style="left:114px;top:74px">Special</span><span class="lb" style="left:153px;top:74px">Single</span>
    <div class="copy" style="left:14px;top:79px;width:150px;height:6px"></div>
  </div><span class="file">Slide21.JPG</span></div>

  <!-- 22 -->
  <div class="cell"><div class="slide">
    <i class="mark"></i><div class="st">Portfolio</div><div class="brand">Norvalo</div>
    <div class="ph" style="left:12px;top:20px;width:48px;height:28px"></div>
    <div class="a green" style="left:60px;top:20px;width:48px;height:28px"></div>
    <div class="ph" style="left:108px;top:20px;width:22px;height:28px"></div>
    <div class="a blue" style="left:130px;top:20px;width:38px;height:28px"></div>
    <div class="a orange" style="left:12px;top:48px;width:48px;height:34px"></div>
    <div class="ph" style="left:60px;top:48px;width:48px;height:34px"></div>
    <div class="a teal" style="left:108px;top:48px;width:22px;height:34px"></div>
    <div class="ph" style="left:130px;top:48px;width:38px;height:34px"></div>
    <span class="lb w" style="left:72px;top:24px">Portfolio II</span><span class="lb w" style="left:138px;top:24px">Portfolio IV</span><span class="lb w" style="left:20px;top:52px">Portfolio I</span><span class="lb w" style="left:110px;top:52px">Portfolio III</span>
  </div><span class="file">Slide22.JPG</span></div>

  <!-- 23 -->
  <div class="cell"><div class="slide">
    <i class="mark"></i><div class="st">Brand Detailed</div><div class="brand">Norvalo</div>
    <div class="ph" style="left:14px;top:20px;width:84px;height:60px"></div>
    <div class="a orange" style="left:98px;top:20px;width:34px;height:30px"></div>
    <div class="a teal" style="left:132px;top:20px;width:34px;height:30px"></div>
    <div class="a green" style="left:98px;top:50px;width:34px;height:30px"></div>
    <div class="a blue" style="left:132px;top:50px;width:34px;height:30px"></div>
    <span class="lb w" style="left:108px;top:24px">Brand</span><span class="lb w" style="left:137px;top:24px">Technology</span><span class="lb w" style="left:108px;top:54px">Leisure</span><span class="lb w" style="left:142px;top:54px">Digital</span>
  </div><span class="file">Slide23.JPG</span></div>

  <!-- 24 -->
  <div class="cell"><div class="slide">
    <i class="mark"></i><div class="st">Recognition</div><div class="brand">Norvalo</div>
    <div class="a green" style="left:12px;top:22px;width:94px;height:24px"></div>
    <div class="ph" style="left:106px;top:22px;width:30px;height:24px"></div>
    <div class="a blue" style="left:136px;top:22px;width:30px;height:48px"></div>
    <div class="a orange" style="left:12px;top:46px;width:22px;height:24px"></div>
    <div class="a orange" style="left:34px;top:46px;width:102px;height:24px;filter:brightness(1.05)"></div>
    <span class="lb w" style="left:16px;top:26px">System Online</span><span class="lb w" style="left:110px;top:50px">Security</span><span class="lb w" style="left:141px;top:50px">Mobile</span>
  </div><span class="file">Slide24.JPG</span></div>

  <!-- 25 -->
  <div class="cell"><div class="slide">
    <i class="mark"></i><div class="st">Accesibility</div><div class="brand">Norvalo</div>
    <svg class="a" style="left:60px;top:20px" width="56" height="64" aria-hidden="true">
      <polygon points="6,6 28,0 50,6 50,14 28,20 6,14" fill="#d8352a"/>
      <polygon points="6,20 28,14 50,20 50,28 28,34 6,28" fill="#f39c1b"/>
      <polygon points="6,34 28,28 50,34 50,42 28,48 6,42" fill="#f5c518"/>
      <polygon points="6,48 28,42 50,48 50,56 28,62 6,56" fill="#1b9e85"/>
    </svg>
    <div class="a" style="left:12px;top:28px;width:40px;height:18px;border:.7px solid var(--red)"></div><span class="lb" style="left:25px;top:30px">System</span>
    <div class="a" style="left:12px;top:56px;width:40px;height:18px;border:.7px solid var(--orange)"></div><span class="lb" style="left:23px;top:58px">Portfolio</span>
    <div class="a" style="left:124px;top:36px;width:40px;height:18px;border:.7px solid var(--orange)"></div><span class="lb" style="left:126px;top:38px">Techniques</span>
    <div class="a" style="left:124px;top:62px;width:40px;height:18px;border:.7px solid var(--teal)"></div><span class="lb" style="left:126px;top:64px">Condition</span>
  </div><span class="file">Slide25.JPG</span></div>

  <!-- 26 -->
  <div class="cell"><div class="slide">
    <i class="mark"></i><div class="st">Digital Cost</div><div class="brand">Norvalo</div>
    <div class="ph" style="left:0;top:20px;width:106px;height:50px"></div>
    <div class="a teal" style="left:106px;top:20px;width:69px;height:50px"></div>
    <i class="ic" style="left:120px;top:24px;background:#fff;width:5px;height:5px"></i><span class="lb w" style="left:116px;top:31px">Warning</span>
    <i class="ic" style="left:150px;top:24px;background:#fff;width:5px;height:5px"></i><span class="lb w" style="left:148px;top:31px">Digital</span>
    <i class="ic" style="left:120px;top:46px;background:#fff;width:5px;height:5px"></i><span class="lb w" style="left:114px;top:53px">Workshop</span>
    <i class="ic" style="left:150px;top:46px;background:#fff;width:5px;height:5px"></i><span class="lb w" style="left:147px;top:53px">Charting</span>
    <div class="copy" style="left:14px;top:78px;width:150px;height:6px"></div>
  </div><span class="file">Slide26.JPG</span></div>

  <!-- 27 -->
  <div class="cell"><div class="slide">
    <i class="mark"></i><div class="st">Business Philosophy</div><div class="brand">Norvalo</div>
    <i class="ic red" style="left:8px;top:22px"></i><span class="lb" style="left:18px;top:22px">Model</span><div class="copy" style="left:18px;top:26px;width:30px;height:5px"></div>
    <i class="ic orange" style="left:8px;top:42px"></i><span class="lb" style="left:18px;top:42px">Document</span><div class="copy" style="left:18px;top:46px;width:30px;height:5px"></div>
    <i class="ic teal" style="left:8px;top:62px"></i><span class="lb" style="left:18px;top:62px">Folder</span><div class="copy" style="left:18px;top:66px;width:30px;height:5px"></div>
    <i class="ic red" style="left:64px;top:22px"></i><span class="lb" style="left:74px;top:22px">Cloud</span><div class="copy" style="left:74px;top:26px;width:30px;height:5px"></div>
    <i class="ic orange" style="left:64px;top:42px"></i><span class="lb" style="left:74px;top:42px">Advance</span><div class="copy" style="left:74px;top:46px;width:30px;height:5px"></div>
    <i class="ic green" style="left:64px;top:62px"></i><span class="lb" style="left:74px;top:62px">Warning</span><div class="copy" style="left:74px;top:66px;width:30px;height:5px"></div>
    <i class="ic slate" style="left:120px;top:22px"></i><span class="lb" style="left:130px;top:22px">Security</span><div class="copy" style="left:130px;top:26px;width:30px;height:5px"></div>
    <i class="ic red" style="left:120px;top:42px"></i><span class="lb" style="left:130px;top:42px">Support</span><div class="copy" style="left:130px;top:46px;width:30px;height:5px"></div>
    <i class="ic orange" style="left:120px;top:62px"></i><span class="lb" style="left:130px;top:62px">Managing</span><div class="copy" style="left:130px;top:66px;width:30px;height:5px"></div>
    <i class="pager"></i>
  </div><span class="file">Slide27.JPG</span></div>

  <!-- 28 -->
  <div class="cell"><div class="slide">
    <i class="mark"></i><div class="st">Worker In Progress</div><div class="brand">Norvalo</div>
    <div class="a" style="left:14px;top:20px;width:20px;height:66px;background:linear-gradient(180deg,#f39c1b 0 45%,#1b9e85 45%);border-radius:8px 8px 2px 2px" role="img" aria-label="Illustration of a standing worker"></div>
    <i class="ic" style="left:46px;top:24px;width:6px;height:6px;border:.8px solid var(--orange)"></i><div class="copy" style="left:55px;top:24px;width:24px;height:6px"></div>
    <i class="ic" style="left:46px;top:38px;width:6px;height:6px;border:.8px solid var(--orange)"></i><div class="copy" style="left:55px;top:38px;width:24px;height:6px"></div>
    <i class="ic" style="left:46px;top:52px;width:6px;height:6px;border:.8px solid var(--orange)"></i><div class="copy" style="left:55px;top:52px;width:24px;height:6px"></div>
    <i class="ic" style="left:46px;top:66px;width:6px;height:6px;border:.8px solid var(--orange)"></i><div class="copy" style="left:55px;top:66px;width:24px;height:6px"></div>
    <span class="lb" style="left:105px;top:20px">SEGMENTATION</span>
    <svg class="a" style="left:96px;top:34px" width="66" height="40" aria-hidden="true">
      <rect x="4" y="14" width="3" height="24" fill="#3c5a82"/><rect x="9" y="24" width="3" height="14" fill="#1b9e85"/>
      <rect x="20" y="20" width="3" height="18" fill="#3c5a82"/><rect x="25" y="28" width="3" height="10" fill="#1b9e85"/>
      <rect x="36" y="10" width="3" height="28" fill="#3c5a82"/><rect x="41" y="22" width="3" height="16" fill="#1b9e85"/>
      <rect x="52" y="4" width="3" height="34" fill="#3c5a82"/><rect x="57" y="18" width="3" height="20" fill="#1b9e85"/>
    </svg>
  </div><span class="file">Slide28.JPG</span></div>

  <!-- 29 -->
  <div class="cell"><div class="slide">
    <i class="mark"></i><div class="st">Staff Skill</div><div class="brand">Norvalo</div>
    <div class="ph" style="left:72px;top:20px;width:32px;height:70px"></div>
    <svg class="a" style="left:0;top:0" width="175" height="98" aria-hidden="true" fill="none" stroke-width="1">
      <polyline points="50,28 60,28 60,40 72,40" stroke="#1b9e85"/>
      <polyline points="50,48 72,48" stroke="#f39c1b"/>
      <polyline points="50,70 60,70 60,58 72,58" stroke="#3c5a82"/>
      <polyline points="104,46 116,46 116,36 126,36" stroke="#d8352a"/>
      <polyline points="104,62 116,62 116,72 126,72" stroke="#1b9e85"/>
    </svg>
    <span class="lb" style="left:16px;top:20px">Managing</span><div class="copy" style="left:16px;top:25px;width:32px;height:6px"></div>
    <span class="lb" style="left:16px;top:42px">Adaptability</span><div class="copy" style="left:16px;top:47px;width:32px;height:6px"></div>
    <span class="lb" style="left:16px;top:64px">Skill</span><div class="copy" style="left:16px;top:69px;width:32px;height:6px"></div>
    <span class="lb" style="left:128px;top:30px">Auditing</span><div class="copy" style="left:128px;top:35px;width:32px;height:6px"></div>
    <span class="lb" style="left:128px;top:66px">Changing</span><div class="copy" style="left:128px;top:71px;width:32px;height:6px"></div>
  </div><span class="file">Slide29.JPG</span></div>

  <!-- 30 -->
  <div class="cell"><div class="slide" style="background:#5b5b5b">
    <div class="big-title" style="top:32px;font-size:6.5px">Boost Philosophy</div>
    <div class="copy" style="left:30px;top:42px;width:115px;height:5px;background:repeating-linear-gradient(rgba(255,255,255,.45) 0 1px,transparent 1px 3px)"></div>
    <i class="ic" style="left:22px;top:55px;width:14px;height:14px;border:1px solid #fff"></i>
    <i class="ic" style="left:52px;top:55px;width:14px;height:14px;border:1px solid #fff"></i>
    <i class="ic" style="left:82px;top:55px;width:14px;height:14px;border:1px solid #fff"></i>
    <i class="ic" style="left:112px;top:55px;width:14px;height:14px;border:1px solid #fff"></i>
    <i class="ic" style="left:142px;top:55px;width:14px;height:14px;border:1px solid #fff"></i>
    <span class="lb w" style="left:14px;top:72px;width:30px;text-align:center">DIGITAL</span><span class="lb w" style="left:44px;top:72px;width:30px;text-align:center">SHIPPING</span><span class="lb w" style="left:74px;top:72px;width:30px;text-align:center">DOCUMENT</span><span class="lb w" style="left:104px;top:72px;width:30px;text-align:center">CLOUD</span><span class="lb w" style="left:134px;top:72px;width:30px;text-align:center">SEARCH</span>
  </div><span class="file">Slide30.JPG</span></div>

  <!-- 31 -->
  <div class="cell"><div class="slide">
    <i class="mark"></i><div class="st">Branding Strategy</div><div class="brand">Norvalo</div>
    <div class="a" style="left:10px;top:22px;width:52px;height:52px;border-radius:50%;background:radial-gradient(circle at 35% 35%,#f39c1b 0 30%,#2a8cc9 31% 100%)" role="img" aria-label="Illustration of interlocking gears"></div>
    <span class="lb" style="left:70px;top:24px;font-weight:700">Talking</span><div class="copy" style="left:70px;top:28px;width:34px;height:5px"></div>
    <span class="lb" style="left:70px;top:44px;font-weight:700">Kill The Competition</span><div class="copy" style="left:70px;top:48px;width:34px;height:5px"></div>
    <span class="lb" style="left:70px;top:64px;font-weight:700">Looking the Customer</span><div class="copy" style="left:70px;top:68px;width:34px;height:5px"></div>
    <div class="a teal" style="left:122px;top:22px;width:44px;height:24px"></div><span class="lb w" style="left:126px;top:25px">COMPONENT</span>
    <div class="a teal" style="left:122px;top:50px;width:44px;height:24px"></div><span class="lb w" style="left:126px;top:53px">OUTPUT SYSTEM</span>
    <i class="pager"></i>
  </div><span class="file">Slide31.JPG</span></div>

  <!-- 32 -->
  <div class="cell"><div class="slide">
    <i class="mark"></i><div class="st">Market Share</div><div class="brand">Norvalo</div>
    <svg class="a" style="left:14px;top:22px" width="150" height="46" aria-hidden="true">
      <line x1="0" y1="45.5" x2="150" y2="45.5" stroke="#999" stroke-width=".6"/>
      <g><rect x="4" y="30" width="4" height="15" fill="#3c5a82"/><rect x="9" y="20" width="4" height="25" fill="#1b9e85"/><rect x="14" y="34" width="4" height="11" fill="#f39c1b"/><rect x="19" y="26" width="4" height="19" fill="#d8352a"/></g>
      <g><rect x="42" y="24" width="4" height="21" fill="#3c5a82"/><rect x="47" y="12" width="4" height="33" fill="#1b9e85"/><rect x="52" y="28" width="4" height="17" fill="#f39c1b"/><rect x="57" y="18" width="4" height="27" fill="#d8352a"/></g>
      <g><rect x="80" y="18" width="4" height="27" fill="#3c5a82"/><rect x="85" y="8" width="4" height="37" fill="#1b9e85"/><rect x="90" y="22" width="4" height="23" fill="#f39c1b"/><rect x="95" y="4" width="4" height="41" fill="#d8352a"/></g>
      <g><rect x="118" y="14" width="4" height="31" fill="#3c5a82"/><rect x="123" y="20" width="4" height="25" fill="#1b9e85"/><rect x="128" y="6" width="4" height="39" fill="#f39c1b"/><rect x="133" y="10" width="4" height="35" fill="#d8352a"/></g>
    </svg>
    <span class="lb" style="left:30px;top:70px">Asian</span><span class="lb" style="left:68px;top:70px">Euro</span><span class="lb" style="left:106px;top:70px">Africa</span><span class="lb" style="left:144px;top:70px">Pacific</span>
    <div class="copy" style="left:18px;top:75px;width:140px;height:6px"></div>
  </div><span class="file">Slide32.JPG</span></div>

  <!-- 33 -->
  <div class="cell"><div class="slide">
    <i class="mark"></i><div class="st">Market Share</div><div class="brand">Norvalo</div>
    <div class="a navy" style="left:14px;top:20px;width:56px;height:8px"></div><span class="lb w" style="left:18px;top:22px">FEATURES</span>
    <div class="a teal" style="left:70px;top:20px;width:32px;height:8px"></div><span class="lb w" style="left:74px;top:22px">PACKAGE I</span>
    <div class="a orange" style="left:102px;top:20px;width:30px;height:8px;filter:brightness(1.05)"></div><span class="lb w" style="left:104px;top:22px">PACKAGE II</span>
    <div class="a orange" style="left:132px;top:20px;width:30px;height:8px"></div><span class="lb w" style="left:134px;top:22px">PACKAGE III</span>
    <div class="a" style="left:14px;top:28px;width:148px;height:48px;background:repeating-linear-gradient(#eee 0 8px,#fff 8px 10px)"></div>
    <span class="lb" style="left:18px;top:30px">Daily Service</span><span class="lb" style="left:18px;top:40px">Free Studio</span><span class="lb" style="left:18px;top:50px">Gold Card</span><span class="lb" style="left:18px;top:60px">Worldwide Area</span><span class="lb" style="left:18px;top:70px">Hidden Admin</span>
    <svg class="a" style="left:70px;top:28px" width="92" height="50" aria-hidden="true" fill="none" stroke-width=".8">
      <circle cx="16" cy="4" r="2.6" stroke="#1b9e85"/><circle cx="47" cy="14" r="2.6" stroke="#f39c1b"/><circle cx="77" cy="4" r="2.6" stroke="#f39c1b"/>
      <circle cx="47" cy="24" r="2.6" stroke="#f39c1b"/><circle cx="77" cy="34" r="2.6" stroke="#f39c1b"/><circle cx="77" cy="44" r="2.6" stroke="#f39c1b"/><circle cx="16" cy="34" r="2.6" stroke="#1b9e85"/>
    </svg>
    <i class="pager"></i>
  </div><span class="file">Slide33.JPG</span></div>

  <!-- 34 -->
  <div class="cell"><div class="slide">
    <i class="mark"></i><div class="st">Industry Circle</div><div class="brand">Norvalo</div>
    <span class="lb" style="left:12px;top:24px">Customer</span><div class="copy" style="left:12px;top:28px;width:32px;height:5px"></div>
    <span class="lb" style="left:12px;top:44px">Subsidiary</span><div class="copy" style="left:12px;top:48px;width:32px;height:5px"></div>
    <span class="lb" style="left:12px;top:64px">Digital</span><div class="copy" style="left:12px;top:68px;width:32px;height:5px"></div>
    <svg class="a" style="left:50px;top:20px" width="120" height="64" aria-hidden="true">
      <g font-size="4" font-family="Open Sans,sans-serif" text-anchor="middle">
        <circle cx="8" cy="9" r="6" fill="none" stroke="#f39c1b" stroke-width=".8"/><text x="8" y="10.5" fill="#f39c1b">50%</text>
        <circle cx="8" cy="31" r="6" fill="none" stroke="#1b9e85" stroke-width=".8"/><text x="8" y="32.5" fill="#1b9e85">66%</text>
        <circle cx="8" cy="53" r="6" fill="none" stroke="#2a8cc9" stroke-width=".8"/><text x="8" y="54.5" fill="#2a8cc9">30%</text>
      </g>
      <g fill="#f39c1b"><use href="#house" x="20" y="3" width="12" height="12"/><use href="#house" x="34" y="3" width="12" height="12"/><use href="#house" x="48" y="3" width="12" height="12"/></g>
      <g fill="#d6d6d6"><use href="#house" x="62" y="3" width="12" height="12"/><use href="#house" x="76" y="3" width="12" height="12"/><use href="#house" x="90" y="3" width="12" height="12"/></g>
      <g fill="#1b9e85"><use href="#house" x="20" y="25" width="12" height="12"/><use href="#house" x="34" y="25" width="12" height="12"/><use href="#house" x="48" y="25" width="12" height="12"/><use href="#house" x="62" y="25" width="12" height="12"/></g>
      <g fill="#d6d6d6"><use href="#house" x="76" y="25" width="12" height="12"/><use href="#house" x="90" y="25" width="12" height="12"/></g>
      <g fill="#2a8cc9"><use href="#house" x="20" y="47" width="12" height="12"/><use href="#house" x="34" y="47" width="12" height="12"/></g>
      <g fill="#d6d6d6"><use href="#house" x="48" y="47" width="12" height="12"/><use href="#house" x="62" y="47" width="12" height="12"/><use href="#house" x="76" y="47" width="12" height="12"/><use href="#house" x="90" y="47" width="12" height="12"/></g>
    </svg>
  </div><span class="file">Slide34.JPG</span></div>

  <!-- 35 -->
  <div class="cell"><div class="slide">
    <i class="mark"></i><div class="st">World Trending</div><div class="brand">Norvalo</div>
    <svg class="a" style="left:14px;top:22px" width="150" height="30" aria-hidden="true">
      <rect x="0" y="0" width="42" height="30" fill="url(#tileBlue)"/>
      <rect x="54" y="0" width="42" height="20" fill="url(#tileGreen)"/>
      <rect x="108" y="0" width="42" height="25" fill="url(#tileOrange)"/>
    </svg>
    <span class="lb" style="left:14px;top:56px;width:42px;text-align:center">Technology</span><span class="lb" style="left:68px;top:56px;width:42px;text-align:center">Baseline</span><span class="lb" style="left:122px;top:56px;width:42px;text-align:center">Attachment</span>
    <div class="copy" style="left:14px;top:61px;width:42px;height:12px"></div><div class="copy" style="left:68px;top:61px;width:42px;height:12px"></div><div class="copy" style="left:122px;top:61px;width:42px;height:12px"></div>
    <i class="pager"></i>
  </div><span class="file">Slide35.JPG</span></div>

  <!-- 36 -->
  <div class="cell"><div class="slide">
    <i class="mark"></i><div class="st">Our Facilities</div><div class="brand">Norvalo</div>
    <div class="a teal" style="left:0;top:20px;width:175px;height:60px"></div>
    <svg class="a" style="left:0;top:20px" width="175" height="60" aria-hidden="true" fill="none" stroke="#fff" stroke-width=".8">
      <rect x="10" y="8" width="6" height="5"/><rect x="10" y="27" width="6" height="5"/><rect x="10" y="46" width="6" height="5"/>
      <rect x="66" y="8" width="6" height="5"/><rect x="66" y="27" width="6" height="5"/><rect x="66" y="46" width="6" height="5"/>
      <rect x="122" y="8" width="6" height="5"/><rect x="122" y="27" width="6" height="5"/><rect x="122" y="46" width="6" height="5"/>
    </svg>
    <span class="lb w" style="left:20px;top:29px">Communication</span><span class="lb w" style="left:20px;top:48px">Digital</span><span class="lb w" style="left:20px;top:67px">Video</span>
    <span class="lb w" style="left:76px;top:29px">Energy</span><span class="lb w" style="left:76px;top:48px">Unified System</span><span class="lb w" style="left:76px;top:67px">Quick Meeting</span>
    <span class="lb w" style="left:132px;top:29px">Quick Repair</span><span class="lb w" style="left:132px;top:48px">Access</span><span class="lb w" style="left:132px;top:67px">Backup</span>
    <div class="copy" style="left:14px;top:84px;width:148px;height:5px"></div>
  </div><span class="file">Slide36.JPG</span></div>

</main>
</body>
</html>
```